Packiging of Dietry Supplemnts - New Swiss Style Design

please make upgraded design from the attched design .
www.lorvinta.com

Target Market(s)

Switzerland & USA

Industry/Entity Type

Vitamins

Font styles to use
Sans Serif

Colors
0054AA
0677BA
7BADD7
CADEEF
E8F1F8
EB3D1F
EC4F4E
F09395
F8D3D4
FCEDEE

Requirements
Must have
• Swiss Style
Should not have
• dont use the old design style or photo

```html
<!DOCTYPE html>
<html lang="en">
<head>
<meta charset="utf-8">
<title>Velmora Hair Collagen – Packaging Layout</title>
<link rel="stylesheet" href="https://fonts.googleapis.com/css2?family=Cinzel:wght@400&family=Alegreya+Sans:wght@400;800&family=Source+Sans+3:wght@300;400;600;700&display=swap">
<style>
  :root {
    --blue-deep: #0054AA;
    --blue-mid: #0677BA;
    --blue-soft: #7BADD7;
    --blue-pale: #CADEEF;
    --blue-mist: #E8F1F8;
    --red-strong: #EB3D1F;
    --red-coral: #EC4F4E;
    --red-soft: #F09395;
    --red-pale: #F8D3D4;
    --red-mist: #FCEDEE;
    --ink-muted: #4a78a6;
    --ink-soft: #5d7f9f;
    --band: rgba(255, 255, 255, 0.55);
    --label-ink: #1a1a1a;
    --ornament: rgba(123, 173, 215, 0.28);
  }
  html, body {
    margin: 0;
    padding: 0;
    width: 1200px;
    height: 900px;
    overflow: hidden;
    background: #ffffff;
  }
  .canvas {
    position: relative;
    width: 1200px;
    height: 900px;
    font-family: "Source Sans 3", sans-serif;
  }
  .view-label {
    position: absolute;
    font-family: "Cinzel", serif;
    font-size: 34px;
    letter-spacing: 2px;
    color: var(--label-ink);
    white-space: nowrap;
  }
  .view-label--front {
    left: 62px; top: 450px;
    transform: translate(-50%, -50%) rotate(-90deg);
  }
  .view-label--side {
    left: 1155px; top: 450px;
    transform: translate(-50%, -50%) rotate(90deg);
  }

  /* Front panel */
  .front-panel {
    position: absolute;
    left: 102px; top: 151px;
    width: 702px; height: 593px;
    overflow: hidden;
    background: linear-gradient(90deg, var(--blue-pale) 0%, #dbe9f5 45%, var(--blue-mist) 100%);
    outline: 1px solid var(--blue-soft);
  }
  .ornament {
    position: absolute;
    background: radial-gradient(ellipse at center, rgba(255,255,255,0) 0%, rgba(255,255,255,0) 30%, var(--ornament) 45%, rgba(255,255,255,0) 70%);
  }
  .front-panel .ornament { left: 440px; top: 40px; width: 260px; height: 510px; }

  .brand {
    position: absolute;
    left: 500px; top: 46px;
    width: 143px;
    text-align: right;
  }
  .brand-name {
    display: block;
    font-weight: 700;
    font-size: 31px;
    line-height: 1;
    color: var(--red-strong);
  }
  .brand-tagline {
    display: block;
    font-size: 11px;
    color: #333;
    margin-top: 2px;
  }

  .title-hair {
    position: absolute;
    left: 35px; top: 103px;
    margin: 0;
    font-family: "Alegreya Sans", sans-serif;
    font-weight: 400;
    font-size: 46px;
    letter-spacing: 3px;
    line-height: 1;
    color: var(--blue-deep);
  }
  .title-collagen {
    position: absolute;
    left: 33px; top: 143px;
    margin: 0;
    font-family: "Alegreya Sans", sans-serif;
    font-weight: 800;
    font-size: 70px;
    letter-spacing: 1px;
    line-height: 1;
    color: var(--blue-deep);
  }
  .title-rule {
    position: absolute;
    left: 0; top: 216px;
    width: 100px; height: 3px;
    background: var(--red-coral);
  }
  .type-banner {
    position: absolute;
    left: 78px; top: 216px;
    width: 357px; height: 43px;
    border-radius: 0 0 0 22px;
    background: linear-gradient(90deg, var(--blue-deep) 0%, var(--blue-mid) 55%, var(--blue-deep) 100%);
    color: var(--blue-mist);
    font-weight: 300;
    font-size: 18px;
    letter-spacing: 11px;
    line-height: 43px;
    text-align: center;
    white-space: nowrap;
  }
  .claim {
    position: absolute;
    left: 34px; top: 319px;
    margin: 0;
    font-size: 18px;
    font-weight: 400;
    color: var(--blue-deep);
  }
  .claim-rule {
    position: absolute;
    left: 35px; top: 355px;
    width: 250px; height: 1px;
    background: var(--red-coral);
  }
  .ingredients {
    position: absolute;
    left: 36px; top: 367px;
    margin: 0; padding: 0;
    list-style: none;
    font-size: 13px;
    line-height: 20px;
    color: var(--ink-muted);
  }
  .ingredients li::before { content: "•"; margin-right: 7px; color: var(--red-coral); }

  .pack-info {
    position: absolute;
    left: 0; top: 530px;
    width: 702px; height: 40px;
    background: var(--band);
    color: var(--ink-soft);
    font-size: 14px;
  }
  .pack-info__item {
    position: absolute;
    top: 50%;
    transform: translate(-50%, -50%);
    white-space: nowrap;
  }
  .pack-info__divider { position: absolute; top: 8px; width: 1px; height: 24px; background: var(--blue-deep); }
  .pack-count { display: flex; align-items: center; gap: 4px; }
  .pack-count__number { font-weight: 700; font-size: 28px; color: var(--red-strong); line-height: 1; }
  .pack-count__unit { font-size: 12px; line-height: 11px; color: var(--ink-soft); }

  /* Side panel */
  .side-panel {
    position: absolute;
    left: 839px; top: 150px;
    width: 286px; height: 612px;
    overflow: hidden;
    background: linear-gradient(90deg, var(--blue-pale) 0%, #dde9f5 50%, var(--blue-mist) 100%);
  }
  .side-panel .ornament { left: 20px; top: 0; width: 250px; height: 560px; }
  .info-block { position: absolute; left: 20px; width: 258px; }
  .info-block h3 {
    margin: 0 0 4px;
    font-size: 11px;
    font-weight: 700;
    color: var(--blue-deep);
  }
  .info-block ul {
    margin: 0; padding: 0 0 0 21px;
    font-size: 10.8px;
    line-height: 13.5px;
    color: var(--blue-deep);
  }
  .info-block li { margin-bottom: 3px; }
  .info-block li::marker { color: var(--red-coral); }
  .info-block--directions { top: 43px; }
  .info-block--precautions { top: 175px; }
  .info-block--storage { top: 367px; }
</style>
</head>
<body>
<div class="canvas">
  <div class="view-label view-label--front">Front</div>
  <div class="view-label view-label--side">Side</div>

  <section class="front-panel">
    <div class="ornament" role="img" aria-label="Faint large four-point star ornament"></div>

    <div class="brand">
      <span class="brand-name">Velmora</span>
      <span class="brand-tagline">swiss supplements</span>
    </div>

    <h1 class="title-hair">HAIR</h1>
    <h2 class="title-collagen">COLLAGEN</h2>
    <div class="title-rule"></div>
    <div class="type-banner">FOOD SUPPLEMENT</div>

    <p class="claim">Helps in Maintaining Healthy &amp; Strong hair</p>
    <div class="claim-rule"></div>
    <ul class="ingredients">
      <li>Hydrolyzed Collagen</li>
      <li>Calcium</li>
      <li>Zinc</li>
      <li>Iron</li>
      <li>Betacarotene</li>
      <li>Vitamin B</li>
    </ul>

    <div class="pack-info">
      <span class="pack-info__item" style="left:185px">Net Wt. 119g</span>
      <span class="pack-info__divider" style="left:282px"></span>
      <span class="pack-info__item pack-count" style="left:358px">
        <span class="pack-count__number">7</span>
        <span class="pack-count__unit">powder<br>sachets</span>
      </span>
      <span class="pack-info__divider" style="left:439px"></span>
      <span class="pack-info__item" style="left:535px">7 sachets of 19g</span>
    </div>
  </section>

  <section class="side-panel">
    <div class="ornament" role="img" aria-label="Faint large four-point star ornament"></div>

    <div class="info-block info-block--directions">
      <h3>Directions For Use:</h3>
      <ul>
        <li>For adults only.</li>
        <li>Take 1 sachet per day, or as directed by the healthcare provider.</li>
        <li>The content of the sachet should be dissolved into a glass of water (250ml) prior administration.</li>
      </ul>
    </div>

    <div class="info-block info-block--precautions">
      <h3>Precautions:</h3>
      <ul>
        <li>Do not exceed the recommended daily dose.</li>
        <li>Do not use the product in case of hypersensitivity to one of the components.</li>
        <li>Food supplements are not intended to substitute a varied, well-balanced diet and a healthy lifestyle.</li>
        <li>Do not use after the expiry date printed on the box.</li>
        <li>Expiry date refers to the unopened and correctly stored product.</li>
      </ul>
    </div>

    <div class="info-block info-block--storage">
      <h3>Storage Conditions:</h3>
      <ul>
        <li>Store in a cool (&lt;25ºC) and dry place, protected from direct sunlight.</li>
        <li>Keep out of reach of children.</li>
      </ul>
    </div>
  </section>
</div>
</body>
</html>
```